Drifting Past Solvane website

A very basic website using the graphics provided. The site would give the user the ability to read a description of the book, read testimonials, About the author, Read chapter 1, link to vendoro, order direct via coinlet.

```html
<!DOCTYPE html>
<html lang="en">
<head>
<meta charset="utf-8">
<title>Drifting Past Solvane</title>
<link rel="stylesheet" href="https://fonts.googleapis.com/css2?family=Cinzel:wght@400&family=Cormorant+Garamond:wght@500&family=Cousine&family=Parisienne&display=swap">
<style>
  :root {
    --hero-bg: #080506;
    --hero-stripe: #1c0c10;
    --band-bg: #380e0e;
    --floor-bg: #2a0909;
    --gold-light: #f4d872;
    --gold: #f2b21c;
    --orange: #c9601a;
    --text: #ffffff;
    --cream: #fbf1d8;
  }
  * { box-sizing: border-box; margin: 0; padding: 0; }
  html, body { width: 1200px; height: 1190px; overflow: hidden; background: var(--hero-bg); }
  .page { position: relative; width: 1200px; height: 1190px; color: var(--text); overflow: hidden; }

  .hero {
    position: absolute; left: 0; top: 0; width: 1200px; height: 528px;
    background: linear-gradient(180deg, #050304 0%, var(--hero-stripe) 55%, #0b0507 100%);
  }
  .cover {
    position: absolute; left: 140px; top: 59px; width: 263px; height: 405px;
    background: linear-gradient(180deg, #2a0c12 0%, #12080a 40%, #0a0506 100%);
    box-shadow: 0 0 24px rgba(0,0,0,.8);
  }
  .cover-title { position: absolute; top: 27px; width: 100%; text-align: center; font-family: "Cinzel", serif; line-height: 1; }
  .cover-title .small { display: block; font-size: 20px; color: var(--gold-light); }
  .cover-title .large { display: block; font-size: 29px; margin-top: 6px; color: var(--gold); }
  .cover-art {
    position: absolute; left: 0; top: 93px; width: 263px; height: 250px;
    background: linear-gradient(180deg, #4f7f95 0%, #3a5f52 45%, #14100d 100%);
  }
  .cover-author {
    position: absolute; bottom: 28px; width: 100%; text-align: center;
    font-family: "Cinzel", serif; font-size: 19px; letter-spacing: 1px; color: #d9d9d9;
  }

  .book-intro { position: absolute; left: 482px; top: 88px; width: 573px; text-align: center; }
  .book-title { font-family: "Cinzel", serif; font-weight: 400; line-height: 1; }
  .book-title .small { display: block; font-size: 26px; color: var(--gold-light); }
  .book-title .large { display: block; font-size: 36px; margin-top: 8px; color: var(--gold); background: linear-gradient(90deg, var(--orange), var(--gold)); -webkit-background-clip: text; background-clip: text; -webkit-text-fill-color: transparent; }
  .book-text { margin-top: 30px; font-family: "Cousine", monospace; font-size: 12.2px; line-height: 18.75px; hyphens: auto; }

  .buy { position: absolute; left: 506px; top: 386px; width: 521px; height: 41px; }
  .buy-label {
    position: absolute; left: 0; top: 0; width: 521px; height: 41px; line-height: 41px;
    text-align: center; font-family: "Cinzel", serif; font-size: 21px; color: var(--cream);
  }

  .about { position: absolute; left: 0; top: 528px; width: 1200px; height: 283px; background: var(--band-bg); z-index: 2; }
  .tape { position: absolute; background: rgba(220,210,215,.35); z-index: 1; }
  .author-photo {
    position: absolute; left: 139px; top: 22px; width: 249px; height: 240px;
    transform: rotate(-8deg); background: var(--cream); padding: 6px; box-shadow: 0 4px 12px rgba(0,0,0,.6);
  }
  .author-photo .fill { width: 100%; height: 100%; background: linear-gradient(135deg, #6e3a2a 0%, #9c6b50 45%, #e8e1cf 100%); }
  .about-title { position: absolute; left: 450px; top: 50px; font-family: "Cinzel", serif; font-weight: 400; font-size: 30px; }
  .about-text { position: absolute; left: 450px; top: 96px; width: 630px; font-family: "Parisienne", cursive; font-size: 16.5px; line-height: 22.5px; }

  .testimonials { position: absolute; left: 0; top: 811px; width: 1200px; height: 379px; background: radial-gradient(ellipse at center, #35100e 0%, var(--floor-bg) 70%); z-index: 1; }
  .testimonial { position: absolute; top: 38px; width: 330px; text-align: center; }
  .testimonial .portrait {
    width: 168px; height: 168px; margin: 0 auto; border-radius: 50%; border: 3px solid var(--gold);
    background: linear-gradient(180deg, #7a4a3a 0%, #b88a6c 50%, #efe7d4 100%);
  }
  .testimonial .name { margin-top: 12px; font-family: "Cormorant Garamond", serif; font-weight: 500; font-size: 25px; line-height: 30px; }
  .testimonial .quote { margin-top: 4px; font-family: "Cousine", monospace; font-size: 12px; line-height: 17.8px; }
</style>
</head>
<body>
<div class="page">

  <section class="hero">
    <div class="cover">
      <div class="cover-title"><span class="small">DRIFTING PAST</span><span class="large">SOLVANE</span></div>
      <div class="cover-art" role="img" aria-label="Cover art: a silhouetted man behind prison bars looking out at a tropical beach"></div>
      <div class="cover-author">ROWAN HALLOWAY</div>
    </div>

    <div class="book-intro">
      <h1 class="book-title"><span class="small">DRIFTING PAST</span><span class="large">SOLVANE</span></h1>
      <p class="book-text">Lorem ipsum dolor sit amet, consectetur adipisicing elit, sed do eiusmod tempor incididunt ut labore et dolore magna aliqua. Ut enim ad minim veniam, quis nostrud exercitation ullamco laboris nisi ut aliquip ex ea commodo consequat. Duis aute irure dolor in reprehenderit in voluptate velit esse cillum dolore eu fugiat nulla pariatur. Lorem ipsum dolor sit amet, consectetur adipisicing elit, sed do eiusmod tempor incididunt ut labore et dolore magna aliqua. Ut enim ad minim veniam, quis nostrud exercitation ullamco laboris nisi ut aliquip ex ea commodo consequat. Duis aute irure dolor in reprehenderit in voluptate velit esse cillum dolore eu fugiat nulla pariatur.</p>
    </div>

    <div class="buy">
      <svg width="521" height="41" viewBox="0 0 521 41" aria-hidden="true">
        <defs>
          <linearGradient id="rule-left" x1="0" x2="1"><stop offset="0" stop-color="#f4d872" stop-opacity="0"/><stop offset="1" stop-color="#f4d872"/></linearGradient>
          <linearGradient id="rule-right" x1="0" x2="1"><stop offset="0" stop-color="#f4d872"/><stop offset="1" stop-color="#f4d872" stop-opacity="0"/></linearGradient>
          <linearGradient id="button-fill" x1="0" x2="1"><stop offset="0" stop-color="#b9500f"/><stop offset="1" stop-color="#f6b81c"/></linearGradient>
        </defs>
        <rect x="0" y="20" width="186" height="1.5" fill="url(#rule-left)"/>
        <rect x="335" y="20" width="186" height="1.5" fill="url(#rule-right)"/>
        <polygon points="194,0 327,0 336,20.5 327,41 194,41 185,20.5" fill="url(#button-fill)"/>
      </svg>
      <span class="buy-label">BUY NOW</span>
    </div>
  </section>

  <section class="about">
    <div class="author-photo"><div class="fill" role="img" aria-label="Portrait photo of the author in a white chef jacket"></div></div>
    <div class="tape" style="left:290px;top:16px;width:104px;height:34px;transform:rotate(35deg);"></div>
    <div class="tape" style="left:128px;top:246px;width:108px;height:32px;transform:rotate(35deg);"></div>
    <h2 class="about-title">ABOUT THE AUTHOR</h2>
    <p class="about-text">Lorem ipsum dolor sit amet, consectetur adipisicing elit, sed do eiusmod tempor incididunt ut labore et dolore magna aliqua. Ut enim ad minim veniam, quis nostrud exercitation ullamco laboris nisi ut aliquip ex ea commodo consequat. Duis aute irure dolor in reprehenderit in voluptate velit esse cillum dolore eu fugiat nulla pariatur dolore eu fugiat. Duis aute irure dolor in reprehenderit in voluptate velit esse cillum dolore eu fugiat nulla pariatur dolore eu fugiat. Duis aute irure dolor in labore reprehenderit in voluptate velit esse cillum dolore eu fugiat nulla pariatur dolore eu fugiat.</p>
  </section>

  <section class="testimonials">
    <article class="testimonial" style="left:108px;">
      <div class="portrait" role="img" aria-label="Reviewer portrait photo"></div>
      <h3 class="name">Miles Thornbury</h3>
      <p class="quote">Lorem ipsum dolor sit amet, consectetur adipisicing elit, sed do eiusmod tempor incididunt ut labore et dolore magna aliqua. Ut enim ad minim veniam</p>
    </article>
    <article class="testimonial" style="left:435px;">
      <div class="portrait" role="img" aria-label="Reviewer portrait photo"></div>
      <h3 class="name">Miles Thornbury</h3>
      <p class="quote">Lorem ipsum dolor sit amet, consectetur adipisicing elit, sed do eiusmod tempor incididunt ut labore et dolore magna aliqua. Ut enim ad minim veniam</p>
    </article>
    <article class="testimonial" style="left:763px;">
      <div class="portrait" role="img" aria-label="Reviewer portrait photo"></div>
      <h3 class="name">Miles Thornbury</h3>
      <p class="quote">Lorem ipsum dolor sit amet, consectetur adipisicing elit, sed do eiusmod tempor incididunt ut labore et dolore magna aliqua. Ut enim ad minim veniam</p>
    </article>
  </section>

</div>
</body>
</html>
```